Birchwood Lodge Rentals Bill Board

7x21 bill board.

Im needing a bill board for a vacation rental company. Specializing in cabin rentals.
Here are the main points I want mentioned on the billboard:

Quality vacation rentals

Accepting new vacation rental homes.

Family owned and operated.

Fernridgestays.com
865-417-3082

Use either logo whichever looks best. Be creative

Target Market(s)

Cabin owners

Industry/Entity Type

Hospitality

Font styles to use
Sans Serif

Requirements
Must have
• Would like the cabin picture to be the background. Must have the fernridge logo, phone number and website

```html
<!DOCTYPE html>
<html lang="en">
<head>
<meta charset="utf-8">
<title>Birchwood Lodge Rentals Billboard</title>
<link href="https://fonts.googleapis.com/css2?family=Tinos:wght@400;700&display=swap" rel="stylesheet">
<style>
  :root {
    --page-mint: #c0dbca;
    --band-sage: #6e937a;
    --panel-black: #000000;
    --accent-mint: #9fd4b3;
    --ink-white: #ffffff;
  }
  * { margin: 0; padding: 0; box-sizing: border-box; }
  html, body { width: 1200px; height: 800px; overflow: hidden; }
  body {
    background: var(--page-mint);
    font-family: "Tinos", "Times New Roman", serif;
    position: relative;
  }
  .billboard {
    position: absolute;
    left: 79px; top: 226px;
    width: 1042px; height: 347px;
    background: var(--band-sage);
    overflow: hidden;
    box-shadow: 0 4px 10px rgba(0,0,0,0.25);
  }
  .cabin-photo {
    position: absolute;
    left: 430px; top: 65px;
    width: 612px; height: 282px;
    background:
      linear-gradient(180deg, rgba(0,0,0,0) 0%, rgba(0,0,0,0) 40%, rgba(60,40,25,0.6) 100%),
      linear-gradient(100deg, #f3a24a 0%, #e3894a 25%, #8a5a3a 50%, #7a4a2a 70%, #5b5560 100%);
  }
  .headline-panel { position: absolute; left: 0; top: 0; }
  .quality-mark {
    position: absolute; left: 23px; top: 18px;
    display: flex; align-items: center; gap: 9px;
    color: var(--ink-white);
  }
  .quality-text { font-size: 21px; line-height: 22px; letter-spacing: 0.3px; white-space: nowrap; }
  .stars { letter-spacing: 1px; margin-left: 10px; font-size: 21px; }
  .contact {
    position: absolute; top: 7px;
    display: flex; align-items: center; gap: 10px;
    color: var(--ink-white); font-size: 21px;
    white-space: nowrap;
  }
  .contact--web { left: 480px; }
  .contact--phone { left: 824px; }
  .contact-icon {
    width: 48px; height: 48px; border-radius: 50%; flex: none;
    background: var(--panel-black);
    display: flex; align-items: center; justify-content: center;
  }
  .accepting {
    position: absolute; left: 64px; top: 98px;
    color: var(--ink-white); font-size: 58px; line-height: 1;
    display: flex; align-items: center; gap: 6px;
  }
  .offer {
    position: absolute; left: 77px; top: 160px; width: 350px;
    color: var(--ink-white); font-size: 42px; line-height: 35px;
    text-align: center; letter-spacing: 0.5px;
  }
  .divider {
    position: absolute; left: 122px; top: 247px;
    width: 259px; height: 2px; background: var(--accent-mint);
  }
  .family {
    position: absolute; left: 90px; top: 261px; width: 326px;
    color: var(--accent-mint); font-size: 28px; line-height: 27px;
    text-align: center; letter-spacing: 1px;
  }
  .brand-name {
    position: absolute; left: 593px; top: 222px; width: 400px;
    color: var(--ink-white); font-size: 34px; line-height: 38px;
    text-align: center; letter-spacing: 2px;
  }
</style>
</head>
<body>
  <div class="billboard">
    <div class="cabin-photo" role="img" aria-label="Photo of a two-storey timber cabin with a dark metal roof on a wooded hillside at sunset, mountains behind"></div>

    <svg class="headline-panel" width="1042" height="347" viewBox="0 0 1042 347" aria-hidden="true">
      <polygon points="0,79 499,79 560,152 436,347 0,347" fill="var(--panel-black)"/>
    </svg>

    <div class="quality-mark">
      <svg width="54" height="38" viewBox="0 0 54 38" aria-hidden="true" fill="none" stroke="var(--ink-white)" stroke-width="2">
        <path d="M8 16 L2 28 H14 Z"/><line x1="8" y1="28" x2="8" y2="36"/>
        <path d="M16 18 L32 4 L50 18"/><path d="M20 16 V36 H48 V16"/>
        <rect x="28" y="24" width="7" height="12"/><rect x="39" y="22" width="6" height="6"/>
        <rect x="40" y="3" width="4" height="8"/>
      </svg>
      <div class="quality-text">QUALITY <span class="stars">★★★★★</span><br>VACATION RENTALS</div>
    </div>

    <div class="contact contact--web">
      <span class="contact-icon">
        <svg width="26" height="26" viewBox="0 0 26 26" fill="none" stroke="var(--ink-white)" stroke-width="1.8" aria-hidden="true">
          <circle cx="13" cy="13" r="11"/><ellipse cx="13" cy="13" rx="5" ry="11"/>
          <line x1="2" y1="13" x2="24" y2="13"/><line x1="4" y1="7.5" x2="22" y2="7.5"/><line x1="4" y1="18.5" x2="22" y2="18.5"/>
        </svg>
      </span>
      <span>FERNRIDGESTAYS.COM</span>
    </div>

    <div class="contact contact--phone">
      <span class="contact-icon">
        <svg width="24" height="24" viewBox="0 0 24 24" fill="none" stroke="var(--ink-white)" stroke-width="1.6" aria-hidden="true">
          <path d="M5 3 L9 3 L10.5 8 L8 9.5 C9.5 12.5 11.5 14.5 14.5 16 L16 13.5 L21 15 L21 19 C21 20 20 21 19 21 C10 20.5 3.5 14 3 5 C3 4 4 3 5 3 Z"/>
        </svg>
      </span>
      <span>865-417-3082</span>
    </div>

    <div class="accepting">
      <span>ACCEPTING</span>
      <svg width="52" height="46" viewBox="0 0 52 46" aria-hidden="true">
        <circle cx="20" cy="26" r="19" fill="var(--accent-mint)"/>
        <path d="M10 24 L19 35 L48 3" fill="none" stroke="var(--band-sage)" stroke-width="7" stroke-linejoin="round"/>
      </svg>
    </div>

    <div class="offer">NEW VACATION<br>RENTAL HOMES</div>
    <div class="divider"></div>
    <div class="family">FAMILY OWNED<br>&amp; OPERATED</div>

    <div class="brand-name">BIRCHWOOD LODGE RENTALS</div>
  </div>
</body>
</html>
```